Flyer für Bikeshop
Zielgruppe
Bikeshop bikevermietung bikereparatur 365/365 offen
Aufgabenstellung
Der beigelegte Flyer sollte professionell gestaltet werden. Gerne sende ich diverse Fotos mit um sie evtl. zu verwenden. Ich habe keine präferenzen. Der Flyer sollte Jugendliche ansprechen. Der Flyer kann auch gänzlich ohne Fotos sein.

```html
<!DOCTYPE html>
<html lang="de">
<head>
<meta charset="utf-8">
<title>Fahrtraining Flyer</title>
<link rel="stylesheet" href="https://fonts.googleapis.com/css2?family=Alfa+Slab+One&family=Poppins:wght@400;500;600;700&display=swap">
<style>
  :root {
    --page: #e6e6e6;
    --ink: #2d2d2d;
    --yellow: #fcc521;
    --yellow-dark: #d99a12;
    --red: #dc3129;
    --white: #ffffff;
    --text-dark: #1f1f1f;
    --slab: "Alfa Slab One", serif;
    --sans: "Poppins", sans-serif;
  }
  * { box-sizing: border-box; margin: 0; padding: 0; }
  html, body { width: 1200px; height: 2317px; overflow: hidden; background: var(--page); }
  .flyer {
    position: absolute; left: 80px; top: 421px;
    width: 1040px; height: 1474px;
    background: var(--ink);
    overflow: hidden;
    box-shadow: 0 6px 18px rgba(0,0,0,.25);
    font-family: var(--sans);
  }
  .flyer-backdrop { position: absolute; inset: 0; }
  .abs { position: absolute; }

  .headline { left: 0; width: 1040px; text-align: center; font-family: var(--slab); line-height: 1; }
  .headline-top { top: 498px; font-size: 84px; color: var(--white); letter-spacing: 2px; }
  .headline-bottom { top: 582px; font-size: 84px; color: var(--yellow); letter-spacing: 2px; }

  .price-box {
    background: var(--red); top: 676px; height: 151px;
    box-shadow: 4px 6px 10px rgba(0,0,0,.45);
    text-align: center; color: var(--white);
  }
  .price-own { left: 52px; width: 518px; }
  .price-rent { left: 606px; width: 376px; }
  .price-label { font-weight: 600; font-size: 38px; line-height: 1; margin-top: 16px; }
  .price-value { font-family: var(--slab); color: var(--yellow); font-size: 76px; line-height: 1; margin-top: 6px; }
  .price-currency { font-size: 30px; margin-right: 8px; }

  .youth-fold { left: 540px; top: 1150px; }
  .youth-box {
    left: 43px; top: 874px; width: 539px; height: 314px;
    background: var(--yellow); border-radius: 30px;
    transform: rotate(-2deg); transform-origin: center;
    text-align: center; padding-top: 46px;
  }
  .youth-title { font-family: var(--slab); color: var(--red); font-size: 92px; line-height: 1; }
  .youth-sub { font-family: var(--slab); color: var(--red); font-size: 46px; line-height: 1; margin-top: 6px; letter-spacing: 1px; }
  .youth-text { font-weight: 600; font-size: 37px; line-height: 1.15; color: var(--text-dark); margin-top: 12px; }

  .feature-list { left: 637px; top: 874px; list-style: none; }
  .feature-list li {
    display: flex; align-items: center; gap: 20px;
    color: var(--white); font-weight: 600; font-size: 32px; height: 49px;
  }
  .feature-list svg { flex: none; }

  .schedule { left: 65px; top: 1222px; color: var(--text-dark); }
  .schedule-day { font-size: 30px; font-weight: 500; line-height: 1.2; }
  .schedule-time { font-size: 48px; font-weight: 700; line-height: 1.1; }
  .schedule-place { font-size: 19px; font-weight: 500; line-height: 1.4; }

  .brand { left: 70px; top: 1380px; display: flex; align-items: center; gap: 14px; }
  .brand-dot { width: 36px; height: 36px; border-radius: 50%; background: var(--text-dark); }
  .brand-name { font-size: 38px; font-weight: 700; color: var(--text-dark); letter-spacing: 6px; }

  .trainer-photo {
    left: 397px; top: 1213px; width: 130px; height: 130px; border-radius: 50%;
    border: 6px solid var(--yellow);
    background: radial-gradient(circle at 50% 40%, #c89a7e, #6a4a36 70%, #3a2a20);
  }
  .trainer { left: 547px; top: 1214px; }
  .trainer-name { font-size: 47px; font-weight: 700; color: var(--text-dark); line-height: 1.1; }
  .trainer-role { font-size: 38px; font-weight: 600; color: var(--red); line-height: 1.1; }
  .trainer-contact { font-size: 20px; font-weight: 500; color: var(--text-dark); margin-top: 4px; }

  .contact-line { left: 450px; display: flex; align-items: center; gap: 12px; font-size: 22px; font-weight: 500; color: var(--text-dark); }
  .contact-address { top: 1370px; }
  .contact-mail { top: 1410px; }
  .contact-phone { margin-left: 20px; display: flex; align-items: center; gap: 12px; }
</style>
</head>
<body>
<main class="flyer">
  <svg class="flyer-backdrop" width="1040" height="1474" viewBox="0 0 1040 1474">
    <defs>
      <linearGradient id="mountainTones" x1="0" y1="0" x2="0" y2="1">
        <stop offset="0" stop-color="#8fb4d8"/>
        <stop offset="0.35" stop-color="#c9d3dc"/>
        <stop offset="0.55" stop-color="#5d8fa6"/>
        <stop offset="1" stop-color="#8a7a4e"/>
      </linearGradient>
    </defs>
    <rect class="hero-photo" role="img" aria-label="Foto: Mountainbiker auf einem Trail über einem Bergsee bei St. Moritz" x="0" y="0" width="1040" height="420" fill="url(#mountainTones)"/>
    <path class="location-band" d="M0,344 Q520,430 1040,340 L1040,432 Q520,505 0,440 Z" fill="var(--yellow)"/>
    <path id="locationCurve" d="M100,414 Q520,478 940,404" fill="none"/>
    <text font-family="Alfa Slab One, serif" font-size="30" letter-spacing="8" fill="#1f1f1f">
      <textPath href="#locationCurve" startOffset="50%" text-anchor="middle">LOCATION AT ST. MORITZ</textPath>
    </text>
    <path class="footer-stripe" d="M0,1196 Q520,1130 1040,1210 L1040,1232 Q520,1152 0,1214 Z" fill="var(--yellow)"/>
    <path class="footer-area" d="M0,1212 Q520,1150 1040,1230 L1040,1474 L0,1474 Z" fill="var(--white)"/>
  </svg>

  <h1 class="abs headline headline-top">FREE BICYCLE</h1>
  <h2 class="abs headline headline-bottom">SKILLS TRAINING</h2>

  <div class="abs price-box price-own">
    <p class="price-label">Mit eigenem Bike</p>
    <p class="price-value">GRATIS</p>
  </div>
  <div class="abs price-box price-rent">
    <p class="price-label">Mit Mietbike</p>
    <p class="price-value"><span class="price-currency">FR.</span>20.-</p>
  </div>

  <svg class="abs youth-fold" width="60" height="60" viewBox="0 0 60 60">
    <path d="M0,20 L50,0 L20,50 Z" fill="var(--yellow-dark)"/>
  </svg>
  <div class="abs youth-box">
    <p class="youth-title">GRATIS</p>
    <p class="youth-sub">FAHRTRAINING</p>
    <p class="youth-text">Fur alle Jugendlichen<br>von 8-14 Jahren</p>
  </div>

  <ul class="abs feature-list">
    <li><svg width="24" height="24" viewBox="0 0 24 24"><circle cx="12" cy="12" r="11" fill="var(--yellow)"/><path d="M7,12 L10.5,15.5 L17,9" stroke="var(--ink)" stroke-width="2.6" fill="none"/></svg>Bremstraining</li>
    <li><svg width="24" height="24" viewBox="0 0 24 24"><circle cx="12" cy="12" r="11" fill="var(--yellow)"/><path d="M7,12 L10.5,15.5 L17,9" stroke="var(--ink)" stroke-width="2.6" fill="none"/></svg>Fahrkurse</li>
    <li><svg width="24" height="24" viewBox="0 0 24 24"><circle cx="12" cy="12" r="11" fill="var(--yellow)"/><path d="M7,12 L10.5,15.5 L17,9" stroke="var(--ink)" stroke-width="2.6" fill="none"/></svg>Wheelytraining</li>
    <li><svg width="24" height="24" viewBox="0 0 24 24"><circle cx="12" cy="12" r="11" fill="var(--yellow)"/><path d="M7,12 L10.5,15.5 L17,9" stroke="var(--ink)" stroke-width="2.6" fill="none"/></svg>Techniktips</li>
    <li><svg width="24" height="24" viewBox="0 0 24 24"><circle cx="12" cy="12" r="11" fill="var(--yellow)"/><path d="M7,12 L10.5,15.5 L17,9" stroke="var(--ink)" stroke-width="2.6" fill="none"/></svg>Reparaturkurse</li>
  </ul>

  <div class="abs schedule">
    <p class="schedule-day">Jeden Freiteg</p>
    <p class="schedule-time">16.30 - 18.30</p>
    <p class="schedule-place">Treffpunkt RADWERK St. Moritz</p>
  </div>

  <div class="abs brand">
    <span class="brand-dot"></span>
    <span class="brand-name">RADWERK</span>
  </div>

  <div class="abs trainer-photo" role="img" aria-label="Porträtfoto der Trainerin"></div>
  <div class="abs trainer">
    <p class="trainer-name">Lina Vastrup</p>
    <p class="trainer-role">Lehrling 1. Jahr</p>
    <p class="trainer-contact">lina@radwerk.ch &nbsp;|&nbsp; 081 555 20 40</p>
  </div>

  <p class="abs contact-line contact-address">
    <svg width="24" height="26" viewBox="0 0 24 26"><path d="M12,1 C6,1 2,5 2,10.5 C2,17 12,25 12,25 C12,25 22,17 22,10.5 C22,5 18,1 12,1 Z" fill="var(--red)"/><circle cx="12" cy="10.5" r="4" fill="var(--white)"/></svg>
    Bergstrasse 12 | 7500 St. Moritz
  </p>
  <p class="abs contact-line contact-mail">
    <svg width="24" height="24" viewBox="0 0 24 24"><circle cx="12" cy="12" r="12" fill="var(--red)"/><rect x="6" y="8" width="12" height="8.5" fill="none" stroke="var(--white)" stroke-width="1.6"/><path d="M6,8 L12,13 L18,8" fill="none" stroke="var(--white)" stroke-width="1.6"/></svg>
    info@radwerk.ch
    <span class="contact-phone">
      <svg width="24" height="24" viewBox="0 0 24 24"><circle cx="12" cy="12" r="12" fill="var(--red)"/><path d="M8,6 L10.5,6 L11.5,9 L10,10.5 C10.8,12.3 11.7,13.2 13.5,14 L15,12.5 L18,13.5 L18,16 C18,17 17,18 16,18 C10.5,17.5 6.5,13.5 6,8 C6,7 7,6 8,6 Z" fill="var(--white)"/></svg>
      081 555 20 40
    </span>
  </p>
</main>
</body>
</html>
```